Influencer Marketing Präsentation
Zielgruppe
Ich: Influencer
Anlass: Weiterbildungs-Tagung
Zielgruppe: Teilnehmer der Digital Marketing-Weiterbildung, welche zeitgleich auch Marketing-Leute sind von Unternehmen, die etwas über Influencer Marketing erfahren möchten.
Aufgabenstellung
Ich benötige eine pfannenfertige PPTX Präsentation für meinen Vortrag an einer Digital-Marketing Tagung!
Die Präsentation ist 20min maximal, plus 10min Q&A. Sie soll cool daherkommen, aber nicht zu verspielt. Die Leute sollen sich auch denken 'wow, der hat nicht nur was als Influencer auf dem Kasten, sondern hat auch eine coole PPT zu seinem Vortrag!' Da den ganzen Tag lang unterschiedliche Leute präsentieren zu verschiedensten Marketing Themen, will ich die Präsentation locker und cool gestalten und nicht zu heftig mit Zahlen und schwerem Inhalt.
Die angehängte PPT ist ein Mix aus zwei 'alten' Präsentationen, welche ich zu dem Thema gemacht habe. Nun gilt es, die coolsten Themen rauszupicken, diese bei Bedarf auf Deutsch zu übersetzen, und allenfalls noch andere Influencer-Marketing Themen, Tips & tricks einzubauen.
Im ersten Slide der angehängten Präsentation siehst Du ein Inhaltsverzeichnis. so stelle ich mir das in etwa vor. bin aber auch offen, das ganze zu straffen!
Hier noch ein Link zu einer online verfügbaren Präsentation, von welcher ich folgende Slides integrieren möchte (anders darstellen und Umtexten bitte, damit man nicht 1:1 kopiert!) https://folienkiste.example/slide/48213907/
Slides: 5, 6, 7, 8, 11. Können auch zusammengefasst werden auf 2-3 slides!
Das fertige Projekt (Präsentation) sollte im PPTX Format angeliefert werden, so dass ich allenfalls noch letzte inhaltliche Korrekturen anbringen kann.

```html
<!DOCTYPE html>
<html lang="de">
<head>
<meta charset="utf-8">
<title>Influencer Marketing – Präsentation</title>
<link rel="stylesheet" href="https://fonts.googleapis.com/css2?family=Fira+Sans+Condensed:wght@400;500&family=Montserrat:wght@400;600;700;800&family=Merriweather:wght@400;700&family=Bitter:wght@400;600&display=swap">
<style>
  :root {
    --page-bg: #ffffff;
    --ink: #111111;
    --grey-label: #9a9a9a;
    --blue: #1a7ee6;
    --handle-red: #e8202a;
    --lavender: #b3a9e5;
    --shadow: 0 2px 10px rgba(0,0,0,0.22);
  }
  * { box-sizing: border-box; margin: 0; padding: 0; }
  html, body { width: 1200px; height: 2400px; overflow: hidden; background: var(--page-bg); }
  body { position: relative; font-family: "Montserrat", sans-serif; color: var(--ink); }

  .slide { position: absolute; left: 115px; width: 1000px; height: 558px; background: #fff; box-shadow: var(--shadow); overflow: hidden; }
  .slide--title { top: 28px; }
  .slide--about { top: 627px; }
  .slide--else { top: 1212px; }
  .slide--start { top: 1808px; }

  /* Title slide */
  .title-photo {
    position: absolute; inset: 0;
    background:
      radial-gradient(ellipse 200px 300px at 800px 330px, rgba(92,104,66,0.95) 0%, rgba(92,104,66,0.7) 55%, rgba(92,104,66,0) 100%),
      radial-gradient(ellipse 150px 170px at 780px 160px, rgba(196,150,120,0.95) 0%, rgba(196,150,120,0.5) 60%, rgba(196,150,120,0) 100%),
      radial-gradient(ellipse 260px 260px at 900px 480px, rgba(86,98,58,1) 0%, rgba(86,98,58,0) 100%),
      radial-gradient(ellipse 200px 130px at 80px 60px, rgba(190,120,100,0.55) 0%, rgba(190,120,100,0) 100%),
      radial-gradient(ellipse 180px 120px at 960px 100px, rgba(120,120,110,0.6) 0%, rgba(120,120,110,0) 100%),
      linear-gradient(180deg, #e4d3c8 0%, #d2c3b7 28%, #c6c2bc 52%, #a8bcc6 68%, #8fb1c4 84%, #a6bfcc 100%);
  }
  .title-card { position: absolute; left: 0; top: 145px; width: 611px; height: 220px; background: #fff; padding: 42px 0 0 44px; }
  .title-card__heading { font-family: "Fira Sans Condensed", sans-serif; font-weight: 400; font-size: 48px; line-height: 1; color: var(--ink); }
  .title-card__claim { font-family: "Merriweather", serif; font-weight: 700; font-size: 30px; color: var(--blue); margin-top: 10px; letter-spacing: 0.4px; }
  .title-card__byline { font-family: Arial, "Helvetica Neue", sans-serif; font-weight: 700; font-size: 19px; margin-top: 22px; }
  .social-handle { position: absolute; left: 38px; top: 458px; display: flex; align-items: center; gap: 9px; font-family: Arial, "Helvetica Neue", sans-serif; font-weight: 700; font-size: 20px; color: var(--handle-red); }
  .social-handle__mark { width: 21px; height: 21px; background: var(--handle-red); border-radius: 4px; }

  /* About slide */
  .about-kicker { position: absolute; top: 22px; width: 100%; text-align: center; font-size: 11px; letter-spacing: 3px; color: var(--grey-label); }
  .about-heading { position: absolute; top: 38px; width: 100%; text-align: center; font-weight: 800; font-size: 33px; color: #1e1e1e; }
  .about-sub { position: absolute; top: 84px; width: 100%; text-align: center; font-family: "Merriweather", serif; font-size: 31px; color: var(--blue); }
  .timeline { position: absolute; inset: 0; }
  .milestone { position: absolute; width: 94px; height: 94px; border-radius: 50%; background: #fff; box-shadow: 0 3px 12px rgba(0,0,0,0.25); display: flex; align-items: center; justify-content: center; font-weight: 700; font-size: 16px; color: var(--blue); transform: translate(-50%, -50%); }
  .milestone__label { position: absolute; transform: translateX(-50%); text-align: center; font-weight: 600; font-size: 12.5px; line-height: 1.2; color: #222; white-space: nowrap; }

  /* What else slide */
  .else-panel { position: absolute; left: 0; top: 0; width: 556px; height: 100%; background: var(--lavender); padding: 120px 0 0 75px; }
  .else-heading { font-family: "Fira Sans Condensed", sans-serif; font-size: 46px; font-weight: 400; color: var(--ink); margin-bottom: 34px; }
  .else-list { list-style: none; font-family: "Bitter", serif; font-size: 23px; line-height: 44.5px; color: #1a1a1a; }
  .else-list strong { font-weight: 600; }
  .else-list s { text-decoration-thickness: 1.5px; }
  .collage-tile { position: absolute; width: 97px; border-radius: 7px; box-shadow: 0 2px 5px rgba(0,0,0,0.2); }

  /* How it started slide */
  .start-heading { position: absolute; top: 16px; width: 100%; text-align: center; font-weight: 800; font-size: 33px; color: #2a2a2a; }
  .story-card { position: absolute; top: 107px; }
  .story-card--ad {
    left: 77px; width: 383px; height: 405px;
    background:
      radial-gradient(ellipse 150px 150px at 190px 150px, rgba(110,110,110,0.55) 0%, rgba(110,110,110,0) 100%),
      radial-gradient(ellipse 160px 90px at 190px 25px, rgba(150,150,150,0.35) 0%, rgba(150,150,150,0) 100%),
      linear-gradient(180deg, #e6e6e6 0%, #cdcdcd 30%, #c4c4c4 50%, #e8e8e8 72%, #ffffff 100%);
  }
  .story-card--first {
    left: 548px; width: 387px; height: 424px;
    background:
      radial-gradient(ellipse 120px 80px at 195px 120px, rgba(214,170,120,0.8) 0%, rgba(214,170,120,0) 100%),
      radial-gradient(ellipse 180px 140px at 100px 170px, rgba(168,120,88,0.6) 0%, rgba(168,120,88,0) 100%),
      radial-gradient(ellipse 180px 140px at 300px 180px, rgba(170,124,92,0.6) 0%, rgba(170,124,92,0) 100%),
      linear-gradient(180deg, #3a2c22 0%, #5e4636 35%, #6f5a47 58%, #71786c 80%, #98aba6 100%);
  }
  .story-card__title { position: absolute; width: 100%; top: 255px; text-align: center; font-family: "Merriweather", serif; font-size: 29px; line-height: 40px; }
  .story-card--ad .story-card__title { color: var(--blue); }
  .story-card--first .story-card__title { color: #fff; top: 253px; }
  .story-card__note { position: absolute; width: 100%; top: 344px; padding: 0 30px; text-align: center; font-weight: 700; font-size: 11.5px; line-height: 15px; }
  .story-card--ad .story-card__note { color: #222; }
  .story-card--first .story-card__note { color: #fff; top: 342px; }
</style>
</head>
<body>

<section class="slide slide--title">
  <div class="title-photo" role="img" aria-label="Foto: Speaker mit Sonnenbrille und grüner Jacke vor einer Altstadt am Fluss"></div>
  <div class="title-card">
    <h1 class="title-card__heading">Influencer Marketing</h1>
    <p class="title-card__claim">DIE KRAFT DER BEEINFLUSSUNG</p>
    <p class="title-card__byline">PFLEGEN DURCH: MARLO</p>
  </div>
  <div class="social-handle"><span class="social-handle__mark"></span>MARLOVENTIS</div>
</section>

<section class="slide slide--about">
  <p class="about-kicker">About Me</p>
  <h2 class="about-heading">WHO AM I?</h2>
  <p class="about-sub">Born and raised in Switzerland</p>
  <svg class="timeline" width="1000" height="558" viewBox="0 0 1000 558">
    <defs>
      <linearGradient id="waveStroke" x1="0" x2="1">
        <stop offset="0" stop-color="#3fb4ea"/>
        <stop offset="0.55" stop-color="#2a8fdc"/>
        <stop offset="1" stop-color="#1565c0"/>
      </linearGradient>
      <linearGradient id="familyBase" x1="0" x2="1">
        <stop offset="0" stop-color="#5d5f60"/>
        <stop offset="0.35" stop-color="#8b7a6c"/>
        <stop offset="0.7" stop-color="#9a8170"/>
        <stop offset="1" stop-color="#c9c8c4"/>
      </linearGradient>
      <radialGradient id="toneDark"><stop offset="0" stop-color="#2b3036" stop-opacity="0.9"/><stop offset="1" stop-color="#2b3036" stop-opacity="0"/></radialGradient>
      <radialGradient id="toneSkin"><stop offset="0" stop-color="#d8a88a" stop-opacity="0.9"/><stop offset="1" stop-color="#d8a88a" stop-opacity="0"/></radialGradient>
      <radialGradient id="tonePink"><stop offset="0" stop-color="#e6b8b4" stop-opacity="0.9"/><stop offset="1" stop-color="#e6b8b4" stop-opacity="0"/></radialGradient>
      <radialGradient id="toneDenim"><stop offset="0" stop-color="#6f8aa6" stop-opacity="0.85"/><stop offset="1" stop-color="#6f8aa6" stop-opacity="0"/></radialGradient>
      <radialGradient id="toneBrown"><stop offset="0" stop-color="#5a3a28" stop-opacity="0.8"/><stop offset="1" stop-color="#5a3a28" stop-opacity="0"/></radialGradient>
      <radialGradient id="toneNavy"><stop offset="0" stop-color="#3c4a66" stop-opacity="0.75"/><stop offset="1" stop-color="#3c4a66" stop-opacity="0"/></radialGradient>
      <clipPath id="waveClip">
        <path d="M0 295 C 40 262, 60 255, 81 263 C 150 280, 210 320, 281 300 C 360 278, 420 245, 490 253 C 570 262, 620 320, 681 325 C 760 330, 820 290, 890 303 C 940 312, 970 340, 1000 338 L1000 558 L0 558 Z"/>
      </clipPath>
    </defs>
    <g clip-path="url(#waveClip)" role="img" aria-label="Familienfoto: Speaker mit Frau und zwei Töchtern">
      <rect x="0" y="240" width="1000" height="318" fill="url(#familyBase)"/>
      <ellipse cx="60" cy="380" rx="120" ry="110" fill="url(#toneDark)"/>
      <ellipse cx="290" cy="380" rx="90" ry="80" fill="url(#toneSkin)"/>
      <ellipse cx="270" cy="510" rx="170" ry="90" fill="url(#toneDenim)"/>
      <ellipse cx="460" cy="420" rx="80" ry="75" fill="url(#toneSkin)"/>
      <ellipse cx="470" cy="530" rx="160" ry="70" fill="url(#tonePink)"/>
      <ellipse cx="670" cy="400" rx="80" ry="80" fill="url(#toneSkin)"/>
      <ellipse cx="620" cy="380" rx="70" ry="90" fill="url(#toneBrown)"/>
      <ellipse cx="760" cy="460" rx="80" ry="75" fill="url(#toneSkin)"/>
      <ellipse cx="770" cy="545" rx="110" ry="60" fill="url(#toneNavy)"/>
    </g>
    <path fill="none" stroke="url(#waveStroke)" stroke-width="9"
      d="M0 295 C 40 262, 60 255, 81 263 C 150 280, 210 320, 281 300 C 360 278, 420 245, 490 253 C 570 262, 620 320, 681 325 C 760 330, 820 290, 890 303 C 940 312, 970 340, 1000 338"/>
  </svg>
  <span class="milestone__label" style="left:81px; top:172px;">HFT Arnau</span>
  <span class="milestone__label" style="left:284px; top:199px;">Hollbrook &amp; Pine<br>USA (Management)</span>
  <span class="milestone__label" style="left:490px; top:163px;">Marketing &amp; Sales<br>(Bus Tour Operator)</span>
  <span class="milestone__label" style="left:681px; top:234px;">Content Creator &amp;<br>Influencer</span>
  <span class="milestone__label" style="left:898px; top:216px;">BrightCore Ltd. (Tech<br>Co., Marketing &amp; Sales)</span>
  <div class="milestone" style="left:81px; top:263px;">2003-06</div>
  <div class="milestone" style="left:281px; top:286px;">2006-10</div>
  <div class="milestone" style="left:490px; top:253px;">2010-19</div>
  <div class="milestone" style="left:681px; top:320px;">2018+</div>
  <div class="milestone" style="left:890px; top:303px;">2020+</div>
</section>

<section class="slide slide--else">
  <div class="else-panel">
    <h2 class="else-heading">WHAT ELSE?</h2>
    <ul class="else-list">
      <li>Married</li>
      <li><strong>Dadlife:</strong> 2 <s>crazy</s> daughters</li>
      <li>No.1 Family Influencer ’22 (Alpine</li>
      <li>Creator Awards ACA)</li>
    </ul>
  </div>
  <div class="collage-tile" role="img" aria-label="Foto: Vater mit Neugeborenem am Meer" style="left:619px; top:56px; height:115px; background:radial-gradient(ellipse 50px 40px at 50% 75%, rgba(214,170,150,0.9), rgba(214,170,150,0)), linear-gradient(#86b6dc 0%, #a9c8de 45%, #7d6a5e 100%);"></div>
  <div class="collage-tile" role="img" aria-label="Foto: Geburtstagsfeier mit Ballons" style="left:619px; top:187px; height:115px; background:radial-gradient(ellipse 20px 18px at 55% 12%, rgba(230,190,70,0.9), rgba(230,190,70,0)), linear-gradient(#e4e0dc 0%, #bfb6ae 50%, #4f5560 100%);"></div>
  <div class="collage-tile" role="img" aria-label="Foto: Paar während der Schwangerschaft" style="left:619px; top:310px; height:115px; background:radial-gradient(ellipse 30px 40px at 65% 55%, rgba(232,180,200,0.9), rgba(232,180,200,0)), linear-gradient(#e8ecef 0%, #d6dadd 50%, #3a3a40 100%);"></div>
  <div class="collage-tile" role="img" aria-label="Foto: Familie auf einer Bergwiese" style="left:724px; top:130px; height:138px; background:radial-gradient(ellipse 40px 45px at 45% 50%, rgba(90,90,95,0.8), rgba(90,90,95,0)), linear-gradient(#9db4be 0%, #b8c2b4 35%, #7f8f58 75%, #6a7a40 100%);"></div>
  <div class="collage-tile" role="img" aria-label="Foto: Familie in Abendkleidung" style="left:724px; top:276px; height:115px; background:radial-gradient(ellipse 40px 30px at 50% 40%, rgba(200,160,140,0.7), rgba(200,160,140,0)), linear-gradient(#5e4a40 0%, #3a302c 60%, #262222 100%);"></div>
  <div class="collage-tile" role="img" aria-label="Foto: Mann mit ausgebreiteten Armen vor Bergpanorama" style="left:724px; top:399px; height:115px; background:radial-gradient(ellipse 30px 22px at 50% 60%, rgba(220,130,90,0.8), rgba(220,130,90,0)), linear-gradient(#8fb6dc 0%, #dde6ee 40%, #b8ac8e 80%, #8e8270 100%);"></div>
  <div class="collage-tile" role="img" aria-label="Foto: Familie mit Fahrzeug vor Chalet" style="left:829px; top:117px; height:115px; background:radial-gradient(ellipse 40px 25px at 45% 80%, rgba(50,50,55,0.8), rgba(50,50,55,0)), linear-gradient(#b9cfe0 0%, #8a6a52 40%, #9c8c80 70%, #6a6864 100%);"></div>
  <div class="collage-tile" role="img" aria-label="Foto: Mutter mit Töchtern am Felsufer" style="left:829px; top:240px; height:115px; background:radial-gradient(ellipse 38px 30px at 45% 65%, rgba(240,200,150,0.85), rgba(240,200,150,0)), linear-gradient(#9dbbd6 0%, #6f94b4 35%, #b49478 70%, #8a6e58 100%);"></div>
</section>

<section class="slide slide--start">
  <h2 class="start-heading">HOW IT STARTED...</h2>
  <div class="story-card story-card--ad" role="img" aria-label="Zeitungsanzeige im Zeichenstil: Mann auf einem Pflug mit Schriftzug">
    <p class="story-card__title">THE FIRST NEW AGE<br>INFLUENCER...</p>
    <p class="story-card__note">June 08, 1918: Harold Fenwick was used as testimonial in a newspaper ad for Orwell Steel Plow Works</p>
  </div>
  <div class="story-card story-card--first" role="img" aria-label="Szene: Gruppe von Männern in historischer Kleidung in einem Raum">
    <p class="story-card__title">THE VERY FIRST<br>INFLUENCER...</p>
    <p class="story-card__note">Analytics through the roof:<br>12 followers, yet worldwide reach...who is it?</p>
  </div>
</section>

</body>
</html>
```